Comic, writer, and entrepreneur based in Los Angeles, CA

UPDATED BRIEF:

Need a PROFESSIONAL yet simultaneously sexy business card that will inspire those to go to my social media accounts and follow me.

Need all of my social media (logos on card, please) As well as my picture, which I will provide.

If there is a way where you could scan the business card from your phone and it would take you to the social media accounts that would be great too!

My goal is to get a comedy writing job at the Nightly Desk or WLR and also go on Pelican Pond once my app is fully functional and created.

But the business card is just something to give people when I am making connections in both the entrepreneurial world as well as the comedy world so it has to help me stand out in that way :).

#: 417-552-8904
Email: kbellin@mx.ovrk.edu
Pictogram: Rosalind_Q.K
Chirpr: @ThePalermoNotes
Craftlo: Rosa’s Clever Tops (website: https://www.craftlo-example.com/shop/RosasTp?ref=pr_shop_more)
VidStream: The Gagmistress (website: https://www.vidstream-example.com/channel/QRpLwVn4kZ-mTHbyqo8erxt7B )
Friendlink: /rosalind.bellin.71924
Website App: WarmFixerFolk.example (app in progress. Need emails to make a prototype.)

Target Market(s)

Talent agents needing TV writers and TV comedy personalities. Investors for my app.

Industry/Entity Type

Tv

Contact Information for Business Card

Can be double or single sided, whichever looks best. Green is my favorite color but I am open to anything. Maybe silver and green?! Just make it classy and sexy.

Colors

Designer to choose colors to be used in the design.

Requirements
Must have
• Chirpr: ThePalermoNotes
• Pictogram: Rosalind_q.k
• Vidstream: The Gagmistress
• Email: kbellin@mx.ovrk.edu
• Phone: 417-552-8904
• writer, comic, entrepreneur--or--comedy writer and entrepeneur
Nice to have
• Make me standout. I'm a star ;-). Please check out my social media for files or ideas. Thanks.

```html
<!DOCTYPE html>
<html lang="en">
<head>
<meta charset="utf-8">
<title>Business Card – Rosalind</title>
<link href="https://fonts.googleapis.com/css2?family=Arimo:wght@400;700&family=Roboto+Condensed:wght@400&display=swap" rel="stylesheet">
<style>
  :root {
    --canvas: #c9d4db;
    --forest: #006f35;
    --lime: #8cc63f;
    --icon-green: #00a651;
    --white: #ffffff;
    --ink: #111111;
    --ink-soft: #333333;
    --photo-warm: #d9b48a;
    --photo-cool: #3a3f9a;
  }
  * { margin: 0; padding: 0; box-sizing: border-box; }
  html, body {
    width: 1200px; height: 882px; overflow: hidden;
    background: var(--canvas);
    font-family: "Arimo", Arial, sans-serif;
  }
  .card {
    position: absolute; left: 100px; top: 140px;
    width: 1000px; height: 601px;
    background: var(--forest);
    overflow: hidden;
    box-shadow: 0 14px 30px rgba(0,0,0,0.25);
  }
  .card-shapes { position: absolute; inset: 0; }
  .identity { position: absolute; left: 71px; top: 58px; color: var(--ink); }
  .identity-name { font-weight: 700; font-size: 36px; line-height: 1; }
  .identity-role { font-size: 27px; color: var(--ink-soft); margin-top: 8px; letter-spacing: -0.5px; }

  .contact {
    position: absolute; right: 48px;
    display: flex; align-items: center; justify-content: flex-end; gap: 11px;
    height: 52px; margin-top: -26px;
    font-size: 28px; color: var(--ink); white-space: nowrap;
  }
  .contact--light { color: var(--white); }
  .contact--condensed { font-family: "Roboto Condensed", "Arial Narrow", sans-serif; font-size: 26px; letter-spacing: -0.4px; }
  .contact--two-line { font-size: 25px; line-height: 28px; text-align: right; }
  .contact-text { display: block; }
  .icon-box {
    flex: none; width: 52px; height: 52px;
    background: var(--icon-green);
    border: 3px solid var(--white);
    outline: 2px solid var(--icon-green);
    outline-offset: -8px;
    display: flex; align-items: center; justify-content: center;
  }
  .icon-box svg { width: 28px; height: 28px; }

  .phone {
    position: absolute; left: 132px; top: 501px;
    display: flex; align-items: center; gap: 25px;
    font-size: 28px; letter-spacing: 0.32em; color: var(--ink);
  }
</style>
</head>
<body>
<div class="card">
  <svg class="card-shapes" width="1000" height="601" viewBox="0 0 1000 601">
    <defs>
      <linearGradient id="portrait-tone" x1="0" y1="0" x2="1" y2="1">
        <stop offset="0" stop-color="#c9a57c"/>
        <stop offset="0.45" stop-color="var(--photo-warm)"/>
        <stop offset="0.8" stop-color="#b88a6a"/>
        <stop offset="1" stop-color="var(--photo-cool)"/>
      </linearGradient>
    </defs>
    <!-- name band -->
    <polygon points="0,36 547,36 597,152 0,152" fill="var(--white)"/>
    <polygon points="553,36 576,36 631,152 601,152" fill="var(--lime)"/>
    <!-- portrait area -->
    <polygon points="0,152 390,152 524,601 136,601" fill="url(#portrait-tone)" role="img" aria-label="Portrait photo of the comedian, smiling"/>
    <!-- contact panel -->
    <polygon points="396,165 1000,165 1000,462 482,462" fill="var(--white)"/>
    <!-- phone band -->
    <polygon points="0,482 672,482 707,581 0,581" fill="var(--white)"/>
    <polygon points="676,482 700,482 738,581 712,581" fill="var(--lime)"/>
  </svg>

  <div class="identity">
    <div class="identity-name">Your Name</div>
    <div class="identity-role">Positions</div>
  </div>

  <div class="contact contact--light" style="top:117px">
    <span class="contact-text">@ThePalermoNotes</span>
    <span class="icon-box" aria-label="Chirpr"></span>
  </div>
  <div class="contact" style="top:194px">
    <span class="contact-text">Rosalind_Q.K</span>
    <span class="icon-box" aria-label="Pictogram"></span>
  </div>
  <div class="contact contact--condensed" style="top:253px">
    <span class="contact-text">/channel/QRpLwVn4kZ-mTHbyqo8erxt7B</span>
    <span class="icon-box" aria-label="VidStream"></span>
  </div>
  <div class="contact" style="top:311px">
    <span class="contact-text">kbellin@mx.ovrk.edu</span>
    <span class="icon-box" aria-label="Email">
      <svg viewBox="0 0 28 28"><rect x="3" y="7" width="22" height="15" fill="none" stroke="#fff" stroke-width="2"/><polyline points="3,7 14,16 25,7" fill="none" stroke="#fff" stroke-width="2"/></svg>
    </span>
  </div>
  <div class="contact" style="top:370px">
    <span class="contact-text">/rosalind.bellin.71924</span>
    <span class="icon-box" aria-label="Friendlink"></span>
  </div>
  <div class="contact contact--two-line" style="top:428px">
    <span class="contact-text">https://www.craftlo-example.com/<br>shop/RosasTp?ref=pr_shop_more</span>
    <span class="icon-box" aria-label="Craftlo shop"></span>
  </div>

  <div class="phone">
    <span class="icon-box" aria-label="Phone">
      <svg viewBox="0 0 28 28"><path d="M8 4c1 0 2 3 3 5 .5 1-1.5 2.5-1 3.5 1 2.5 3 4.5 5.5 5.5 1 .5 2.5-1.5 3.5-1 2 1 5 2 5 3 0 2-2.5 4-4.5 4C11 24 4 17 4 8.5 4 6.5 6 4 8 4z" fill="#fff"/></svg>
    </span>
    <span>417-552-8904</span>
  </div>
</div>
</body>
</html>
```